Crestwell Renewal Business Card Design Phase 2

Professional and clean design. The design colors should flow with the logo. Two-sided card with the website on the back which is:

www.CrestwellRenewal.example.

"Specializing in Water Damage Restoration"

On the front I need the name, email, phone, and logo.

Name: Dorian Halvek
Email: Dorian@CrestwellRenewal.example
Phone: 555-318-2046 for now

I only have the Preview and Thumbnail right now but should have the source files uploaded within a day or two.

Target Market(s)

Flood victims, home owners with water damage from busted pipes etc...

Industry/Entity Type

Business

Contact Information for Business Card

Name: Dorian Halvek

Font styles to use
Serif
Sans Serif

Requirements
Must have
• Business Card Details Info

```html
<!DOCTYPE html>
<html lang="en">
<head>
<meta charset="utf-8">
<title>Crestwell Renewal – Business Card</title>
<link href="https://fonts.googleapis.com/css2?family=Open+Sans:wght@400;600;700;800&family=Playfair+Display:wght@400&display=swap" rel="stylesheet">
<style>
  :root{
    --green:#4f8f3f;
    --navy:#1e3563;
    --white:#ffffff;
    --paper:#ffffff;
    --backdrop:#e9ebe8;
    --ink-soft:#2b3f6b;
  }
  *{margin:0;padding:0;box-sizing:border-box;}
  html,body{width:1200px;height:900px;overflow:hidden;}
  body{
    background:var(--backdrop);
    font-family:"Open Sans",sans-serif;
    display:flex;flex-direction:column;align-items:center;justify-content:center;gap:36px;
  }
  .card{
    position:relative;width:700px;height:400px;overflow:hidden;
    box-shadow:0 10px 28px rgba(0,0,0,.18);
  }

  /* Back side */
  .card-back{background:var(--green);color:var(--white);}
  .card-back .brand{
    position:absolute;top:120px;left:0;right:0;
    display:flex;align-items:center;justify-content:center;gap:14px;
  }
  .brand-mark{width:22px;height:22px;background:currentColor;}
  .brand-name{
    font-weight:800;font-size:50px;letter-spacing:1px;text-transform:uppercase;line-height:1;
  }
  .card-back .tagline{
    position:absolute;left:0;right:0;top:300px;text-align:center;
    font-family:"Playfair Display",serif;font-size:13px;letter-spacing:3px;text-transform:uppercase;
  }
  .card-back .website{
    position:absolute;left:0;right:0;top:324px;text-align:center;
    font-size:17px;font-weight:600;letter-spacing:.5px;
  }

  /* Front side */
  .card-front{background:var(--paper);}
  .front-decor{position:absolute;inset:0;}
  .card-front .brand{
    position:absolute;left:44px;top:150px;color:var(--navy);
    display:flex;align-items:center;gap:12px;
  }
  .card-front .brand-name{font-size:40px;}
  .card-front .brand-mark{width:18px;height:18px;}
  .contact{position:absolute;left:405px;top:200px;}
  .person-name{
    font-weight:800;font-size:22px;text-transform:uppercase;letter-spacing:.5px;margin-bottom:10px;
  }
  .person-name .first{color:var(--green);}
  .person-name .last{color:var(--navy);}
  .contact-line{
    display:flex;align-items:center;gap:10px;color:var(--ink-soft);font-size:15px;line-height:24px;
  }
  .contact-line svg{width:12px;height:12px;flex:none;fill:var(--green);}
</style>
</head>
<body>

  <section class="card card-back" aria-label="Card back">
    <div class="brand">
      <span class="brand-mark"></span>
      <span class="brand-name">Crestwell Renewal</span>
    </div>
    <p class="tagline">Specializing in Water Damage Restoration</p>
    <p class="website">www.CrestwellRenewal.example</p>
  </section>

  <section class="card card-front" aria-label="Card front">
    <svg class="front-decor" width="700" height="400" viewBox="0 0 700 400">
      <polygon points="300,0 700,0 700,14 314,14" fill="#4f8f3f"/>
      <line x1="0" y1="22" x2="700" y2="22" stroke="#4f8f3f" stroke-width="1.5"/>
      <line x1="0" y1="330" x2="700" y2="330" stroke="#4f8f3f" stroke-width="1.5"/>
      <polygon points="0,382 460,382 440,400 0,400" fill="#1e3563"/>
    </svg>

    <div class="brand">
      <span class="brand-mark"></span>
      <span class="brand-name">Crestwell Renewal</span>
    </div>

    <div class="contact">
      <p class="person-name"><span class="first">Dorian</span> <span class="last">Halvek</span></p>
      <p class="contact-line">
        <svg viewBox="0 0 24 24"><path d="M6.6 10.8a15.1 15.1 0 0 0 6.6 6.6l2.2-2.2c.3-.3.7-.4 1-.2 1.1.4 2.3.6 3.6.6.6 0 1 .4 1 1V20c0 .6-.4 1-1 1A17 17 0 0 1 3 4c0-.6.4-1 1-1h3.5c.6 0 1 .4 1 1 0 1.3.2 2.5.6 3.6.1.3 0 .7-.2 1z"/></svg>
        555-318-2046
      </p>
      <p class="contact-line">
        <svg viewBox="0 0 24 24"><path d="M2 5h20v14H2zm2 2v.5l8 5 8-5V7zm0 3v7h16v-7l-8 5z"/></svg>
        Dorian@CrestwellRenewal.example
      </p>
      <p class="contact-line">
        <svg viewBox="0 0 24 24"><path d="M12 2a10 10 0 1 0 0 20 10 10 0 0 0 0-20zm6.9 9h-3a15 15 0 0 0-1.3-5.6A8 8 0 0 1 18.9 11zM12 4.1c.9 1.2 1.8 3.6 1.9 6.9h-3.8c.1-3.3 1-5.7 1.9-6.9zM9.4 5.4A15 15 0 0 0 8.1 11h-3a8 8 0 0 1 4.3-5.6zM5.1 13h3a15 15 0 0 0 1.3 5.6A8 8 0 0 1 5.1 13zm6.9 6.9c-.9-1.2-1.8-3.6-1.9-6.9h3.8c-.1 3.3-1 5.7-1.9 6.9zm2.6-1.3a15 15 0 0 0 1.3-5.6h3a8 8 0 0 1-4.3 5.6z"/></svg>
        www.CrestwellRenewal.example
      </p>
    </div>
  </section>

</body>
</html>
```